Simplified Double Diamond Diagram for Book

I need a simplified version of the Double Diamond Diagram for a book I am working on. I would like to represent the diagram with the following image/text:
- Two diamonds connected (as in each of the sample photos)
- Inclusion of "Diverge" "Converge" above each of the sides of the diamonds as shown in sample image 1 - without elaborative text
- Inclusion of "Problem" and "Solution" in each diamond as is shown in the example image 2
- I need a color version and black/white version of the image that can be turned into a mono-color version in the book.

```html
<!DOCTYPE html>
<html lang="en">
<head>
<meta charset="utf-8">
<title>Double Diamond – Problem and Solution</title>
<link rel="stylesheet" href="https://fonts.googleapis.com/css2?family=Montserrat:wght@800;900&display=swap">
<style>
  :root {
    --page: #ffffff;
    --problem-diverge: #0a79b6;
    --problem-converge: #123f8f;
    --problem-edge: #2b2374;
    --solution-diverge: #98c24e;
    --solution-converge: #62ad3b;
    --solution-edge: #2a8a2b;
    --mono-ink: #1c1a1f;
    --mono-divider: #9a9a9a;
    --label-on-fill: #ffffff;
  }
  html, body {
    margin: 0;
    padding: 0;
    width: 1200px;
    height: 1200px;
    overflow: hidden;
    background: var(--page);
  }
  .diagram-sheet {
    display: block;
    width: 1200px;
    height: 1200px;
  }
  .phase-label,
  .diamond-title {
    font-family: "Montserrat", "Arial Black", sans-serif;
    font-weight: 900;
    text-anchor: middle;
    dominant-baseline: central;
  }
  .phase-label { font-size: 34px; letter-spacing: 0.5px; }
  .diamond-title { font-size: 32px; letter-spacing: 0.3px; }

  .diamond-edge { fill: none; stroke-width: 11; stroke-linejoin: miter; }

  .color .problem .half-diverge { fill: var(--problem-diverge); }
  .color .problem .half-converge { fill: var(--problem-converge); }
  .color .problem .diamond-edge { stroke: var(--problem-edge); }
  .color .problem .phase-label { fill: var(--problem-edge); }

  .color .solution .half-diverge { fill: var(--solution-diverge); }
  .color .solution .half-converge { fill: var(--solution-converge); }
  .color .solution .diamond-edge { stroke: var(--solution-edge); }
  .color .solution .phase-label { fill: var(--solution-edge); }

  .color .diamond-title { fill: var(--label-on-fill); }

  .mono .diamond-edge { stroke: var(--mono-ink); }
  .mono .phase-label,
  .mono .diamond-title { fill: var(--mono-ink); }
  .mono .center-divider { stroke: var(--mono-divider); stroke-width: 1.5; }
</style>
</head>
<body>
<svg class="diagram-sheet" viewBox="0 0 1240 1240" xmlns="http://www.w3.org/2000/svg" role="img" aria-label="Double diamond diagram: Problem and Solution, each with Diverge and Converge phases, in colour and in black and white">
  <defs>
    <g id="diamond-labels">
      <text class="phase-label" transform="translate(265 197) rotate(-45)">DIVERGE</text>
      <text class="phase-label" transform="translate(535 199) rotate(45)">CONVERGE</text>
    </g>
  </defs>

  <!-- Colour version -->
  <g class="color">
    <g class="problem">
      <polygon class="half-diverge" points="399,115 182,332 399,549"/>
      <polygon class="half-converge" points="399,115 616,332 399,549"/>
      <polygon class="diamond-edge" points="399,118 185,332 399,546 613,332"/>
      <use href="#diamond-labels"/>
      <text class="diamond-title" x="399" y="332">PROBLEM</text>
    </g>
    <g class="solution" transform="translate(443 0)">
      <polygon class="half-diverge" points="399,115 182,332 399,549"/>
      <polygon class="half-converge" points="399,115 616,332 399,549"/>
      <polygon class="diamond-edge" points="399,118 185,332 399,546 613,332"/>
      <use href="#diamond-labels"/>
      <text class="diamond-title" x="399" y="332">SOLUTION</text>
    </g>
  </g>

  <!-- Black and white version -->
  <g class="mono" transform="translate(0 575)">
    <g class="problem">
      <line class="center-divider" x1="399" y1="118" x2="399" y2="292"/>
      <line class="center-divider" x1="399" y1="372" x2="399" y2="546"/>
      <polygon class="diamond-edge" points="399,118 185,332 399,546 613,332"/>
      <use href="#diamond-labels"/>
      <text class="diamond-title" x="399" y="332">PROBLEM</text>
    </g>
    <g class="solution" transform="translate(443 0)">
      <line class="center-divider" x1="399" y1="118" x2="399" y2="292"/>
      <line class="center-divider" x1="399" y1="372" x2="399" y2="546"/>
      <polygon class="diamond-edge" points="399,118 185,332 399,546 613,332"/>
      <use href="#diamond-labels"/>
      <text class="diamond-title" x="399" y="332">SOLUTION</text>
    </g>
  </g>
</svg>
</body>
</html>
```